Core Values superheroes - visualizing core values

We are looking to take our core values and come up with creative visuals, superheroes, etc to represent our core values.
Core values and an example attached.
Updates
I have slightly changed my goal for this project. I would like a visual to represent each core value, not a super hero specifically. I will try to post an example in the attachments.
Thank you all for your help and time :)
RT
Target Market(s)
Employees
Industry/Entity Type
Landscape / Lawn care
Look and feel
Each slider illustrates characteristics of the customer's brand and the style your logo design should communicate.

```html
<!DOCTYPE html>
<html lang="en">
<head>
<meta charset="utf-8">
<title>Core Values Poster</title>
<link href="https://fonts.googleapis.com/css2?family=Anton&family=Poppins:wght@300;400;700&display=swap" rel="stylesheet">
<style>
  :root {
    --page-bg: #f4f4f2;
    --poster-bg: #ffffff;
    --sky-blue: #3d5587;
    --sky-blue-light: #4f6a9e;
    --gold-top: #ffe000;
    --gold-bottom: #f6b000;
    --gold: #f7be00;
    --ink: #1f1f1f;
    --white: #ffffff;
  }
  * { margin: 0; padding: 0; box-sizing: border-box; }
  html, body { width: 857px; height: 1200px; overflow: hidden; }
  body {
    background: var(--page-bg);
    font-family: "Poppins", Arial, sans-serif;
    color: var(--ink);
    position: relative;
  }
  .poster {
    position: absolute;
    left: 28px;
    top: 317px;
    width: 800px;
    height: 565px;
    background: var(--poster-bg);
    overflow: hidden;
    box-shadow: 0 14px 22px rgba(0,0,0,0.25);
  }
  .poster > * { position: absolute; }
  .sky-backdrop {
    left: 0; top: 0;
    width: 800px; height: 330px;
    background:
      radial-gradient(ellipse at 50% 0%, var(--sky-blue-light) 0%, var(--sky-blue) 60%),
      var(--sky-blue);
    -webkit-mask-image: linear-gradient(to bottom, #000 0%, #000 62%, transparent 100%);
            mask-image: linear-gradient(to bottom, #000 0%, #000 62%, transparent 100%);
  }
  .title {
    left: 74px; top: 30px;
    font-family: "Anton", Impact, sans-serif;
    font-size: 118px;
    line-height: 1;
    letter-spacing: 7px;
    background: linear-gradient(to bottom, var(--gold-top), var(--gold-bottom));
    -webkit-background-clip: text;
            background-clip: text;
    color: transparent;
    white-space: nowrap;
  }
  .company {
    left: 77px; top: 146px;
    font-weight: 700;
    font-size: 26px;
    line-height: 1.05;
    color: var(--white);
  }
  .company-line { display: block; }

  .hero { border-radius: 40% 40% 18% 18%; }
  .hero-green  { left: 25px;  top: 292px; width: 92px; height: 142px; background: linear-gradient(160deg, #5cb83c, #2f7a2a 60%, #4a4a4a); }
  .hero-yellow { left: 272px; top: 317px; width: 68px; height: 124px; background: linear-gradient(170deg, #e0372a 0%, #f2d22a 30%, #2c6fc4 75%, #f2d22a); }
  .hero-violet { left: 504px; top: 265px; width: 86px; height: 169px; background: linear-gradient(170deg, #8a8a96 0%, #7a3fa6 35%, #e9e9ee 80%); }
  .hero-sky    { left: 212px; top: 434px; width: 60px; height: 109px; background: linear-gradient(170deg, #e0372a 0%, #37a6dd 40%, #f2b62a 70%, #37a6dd); }
  .hero-red    { left: 436px; top: 434px; width: 61px; height: 118px; background: linear-gradient(170deg, #8a8a96 0%, #d93028 35%, #2c4fa0 55%, #d93028 80%); }
  .hero-plum   { left: 683px; top: 441px; width: 71px; height: 114px; background: linear-gradient(170deg, #6b3a25 0%, #6a35a8 40%, #9a2a55 85%); }

  .value { line-height: 1; }
  .value-name { font-size: 18.5px; font-weight: 400; color: var(--ink); display: block; }
  .value-accent { font-size: 18.5px; font-weight: 700; color: var(--gold); display: block; }
  .value-desc { font-size: 10.4px; font-weight: 400; line-height: 12.6px; color: var(--ink); display: block; margin-top: 6px; }

  .v-echale   { left: 128px; top: 364px; }
  .v-community{ left: 352px; top: 364px; }
  .v-impact   { left: 599px; top: 364px; }
  .v-relations{ left: 56px;  top: 470px; }
  .v-right    { left: 303px; top: 470px; }
  .v-solution { left: 528px; top: 457px; }
  .v-community .value-desc,
  .v-impact .value-desc { margin-top: 4px; }
</style>
</head>
<body>
  <main class="poster">
    <div class="sky-backdrop" role="img" aria-label="Comic sunburst background in navy blue with a white city skyline silhouette and the Statue of Liberty"></div>

    <h1 class="title">CORE VALUES</h1>
    <div class="company">
      <span class="company-line">WESTBROOK</span>
      <span class="company-line">GREENS</span>
    </div>

    <div class="hero hero-green" role="img" aria-label="Illustrated superhero in a green suit and grey cape"></div>
    <div class="value v-echale">
      <span class="value-name">ECHALE</span>
      <span class="value-accent">GANAS</span>
      <span class="value-desc">give it your all, every day</span>
    </div>

    <div class="hero hero-yellow" role="img" aria-label="Illustrated kid superhero in a yellow and blue suit saluting"></div>
    <div class="value v-community">
      <span class="value-accent">COMMUNITY</span>
      <span class="value-desc">create community within,<br>while supporting the com-<br>munities we work in</span>
    </div>

    <div class="hero hero-violet" role="img" aria-label="Illustrated superhero in a purple and white suit"></div>
    <div class="value v-impact">
      <span class="value-accent">IMPACT</span>
      <span class="value-desc">building a brighter /<br>greener future for our<br>customers and families</span>
    </div>

    <div class="value v-relations">
      <span class="value-name">RELATIONSHIPS</span>
      <span class="value-accent">FIRST</span>
      <span class="value-desc">give it your all, every day</span>
    </div>
    <div class="hero hero-sky" role="img" aria-label="Illustrated superhero in a light blue suit running"></div>

    <div class="value v-right">
      <span class="value-name">RIGHT</span>
      <span class="value-accent">WAY</span>
      <span class="value-desc">do things the right way,<br>the first time</span>
    </div>
    <div class="hero hero-red" role="img" aria-label="Illustrated superhero in a red and blue suit standing ready"></div>

    <div class="value v-solution">
      <span class="value-name">FIND THE</span>
      <span class="value-accent">SOLUTION</span>
      <span class="value-desc">not knowing how to fix / do<br>something is no excuse to<br>not finding a solution</span>
    </div>
    <div class="hero hero-plum" role="img" aria-label="Illustrated superhero in a purple suit crouching"></div>
  </main>
</body>
</html>
```